Business card design for Automotive workshop

We need a business card for a new automotive repair and tyre shop called Keelstone Prime Automotive located in New Zealand. We are a clean, modern and fresh workshop and company.

Front needs to feature logo,
my name:
Marlo Fitzgerald (director)

Address:
42 Tamsin Road
Whitianga 3510

Phone: 07 541 2298
Mobile: 027 419 5073
Email: office@keelstoneautomotive.co.nz
Website: keelstoneautomotive.co.nz

Back needs to feature an area to write down appointment details, date and time.

Also feature a list of jobs and work we do such as,
Vehicle Servicing
All Mechanical Repairs
Warrant of Fitness
Tyres & Wheel Alignments
Automotive Diagnostics
Automotive Parts & Supplies

```html
<!DOCTYPE html>
<html lang="en">
<head>
<meta charset="utf-8">
<title>Keelstone Prime Automotive – Business Card</title>
<link href="https://fonts.googleapis.com/css2?family=Open+Sans:wght@400;600;700&display=swap" rel="stylesheet">
<style>
  :root {
    --stage: #1b1b1b;
    --card-dark: #1f1f1f;
    --card-light: #ffffff;
    --brand-red: #e3151f;
    --ink: #2a2a2a;
    --ink-soft: #555555;
    --silver: #9a9a9a;
    --silver-light: #d6d6d6;
    --pill: #8e8e8e;
    --rule: #cfcfcf;
  }
  * { box-sizing: border-box; margin: 0; padding: 0; }
  html, body {
    width: 1200px; height: 900px; overflow: hidden;
    background: var(--stage);
    font-family: "Open Sans", Arial, sans-serif;
  }
  .canvas {
    position: relative; width: 1200px; height: 900px;
  }
  .card {
    position: absolute; left: 320px;
    width: 560px; height: 320px;
    border-radius: 3px;
    box-shadow: 0 14px 30px rgba(0,0,0,.55);
  }

  /* Back of card */
  .card-back {
    top: 100px;
    background: var(--card-dark);
    color: var(--silver-light);
    text-align: center;
    padding-top: 52px;
  }
  .card-back .wordmark {
    font-weight: 700; font-size: 26px; letter-spacing: 1px;
    color: var(--silver); text-transform: uppercase;
  }
  .services {
    margin-top: 24px;
    font-size: 14px; line-height: 1.55;
    color: var(--silver-light);
  }
  .services .dot { margin: 0 4px; }
  .appointment {
    position: relative; margin-top: 26px; height: 90px;
  }
  .appointment-title {
    font-weight: 700; font-size: 17px; color: var(--silver);
    letter-spacing: .5px;
  }
  .field {
    position: absolute; display: flex; align-items: center; gap: 10px;
    font-size: 17px; color: var(--silver-light);
  }
  .field-date { left: 70px; top: 40px; }
  .field-time { right: 60px; top: 40px; }
  .pill {
    width: 110px; height: 32px; border-radius: 16px; background: var(--pill);
  }

  /* Front of card */
  .card-front {
    top: 480px;
    background: var(--card-light);
    display: flex; align-items: center;
  }
  .brand {
    width: 290px; padding-left: 34px;
  }
  .brand .wordmark {
    font-weight: 700; font-size: 21px; line-height: 1.2;
    color: var(--brand-red); text-transform: uppercase; letter-spacing: .5px;
  }
  .divider {
    width: 1px; height: 170px; background: var(--rule);
  }
  .contact {
    padding-left: 20px; color: var(--ink);
  }
  .contact .name {
    font-weight: 700; font-size: 18px; color: var(--brand-red); letter-spacing: .3px;
  }
  .contact .role { font-size: 13px; color: var(--ink-soft); margin-bottom: 8px; }
  .contact .address { font-size: 14px; line-height: 1.4; margin-bottom: 8px; }
  .contact-list { list-style: none; font-size: 14px; line-height: 1.45; }
  .contact-list li { display: flex; align-items: center; gap: 7px; }
  .contact-list svg { width: 12px; height: 12px; fill: var(--brand-red); flex: none; }
</style>
</head>
<body>
<main class="canvas">

  <section class="card card-back" aria-label="Card back">
    <div class="wordmark">Keelstone Prime Automotive</div>
    <p class="services">
      Vehicle Servicing<span class="dot">●</span>All Mechanical Repairs<span class="dot">●</span>Warrant of Fitness<br>
      Tyres &amp; Wheel Alignments<span class="dot">●</span>Automotive Diagnostics<br>
      Automotive Parts &amp; Supplies
    </p>
    <div class="appointment">
      <div class="appointment-title">NEXT APPOINTMENT</div>
      <div class="field field-date">DATE <span class="pill"></span></div>
      <div class="field field-time">TIME <span class="pill"></span></div>
    </div>
  </section>

  <section class="card card-front" aria-label="Card front">
    <div class="brand">
      <div class="wordmark">Keelstone Prime<br>Automotive</div>
    </div>
    <div class="divider"></div>
    <div class="contact">
      <div class="name">MARLO FITZGERALD</div>
      <div class="role">Director</div>
      <div class="address">42 Tamsin Road<br>Whitianga 3510</div>
      <ul class="contact-list">
        <li><svg viewBox="0 0 24 24" aria-hidden="true"><path d="M6.6 10.8a15.1 15.1 0 0 0 6.6 6.6l2.2-2.2a1 1 0 0 1 1-.25 11.4 11.4 0 0 0 3.6.57 1 1 0 0 1 1 1V20a1 1 0 0 1-1 1A17 17 0 0 1 3 4a1 1 0 0 1 1-1h3.5a1 1 0 0 1 1 1c0 1.25.2 2.45.57 3.57a1 1 0 0 1-.25 1z"/></svg>07 541 2298</li>
        <li><svg viewBox="0 0 24 24" aria-hidden="true"><path d="M7 1h10a2 2 0 0 1 2 2v18a2 2 0 0 1-2 2H7a2 2 0 0 1-2-2V3a2 2 0 0 1 2-2zm0 3v14h10V4z"/></svg>027 419 5073</li>
        <li><svg viewBox="0 0 24 24" aria-hidden="true"><path d="M2 4h20v16H2zm2 2v.5l8 5.5 8-5.5V6zm0 3v9h16V9l-8 5.5z"/></svg>office@keelstoneautomotive.co.nz</li>
        <li><svg viewBox="0 0 24 24" aria-hidden="true"><circle cx="12" cy="12" r="10"/></svg>keelstoneautomotive.co.nz</li>
      </ul>
    </div>
  </section>

</main>
</body>
</html>
```